Corporate consulting business needs a business card

I want a professional business card.... surprise me

Updates

Reason: i dont think 2 days is enough

Target Market(s)

Corprorate and Not for Profit firms and organisations

Industry/Entity Type

Consulting

Contact Information for Business Card

Logo
Corporate Consulting Services
On Time, On Budget, Beyond Expectation
Tovan Presfield
Director
0427 31 94 62 (Larger)
tovan@tp-advisory.com.au
www.tp-advisory.com.au
include little icons beside the contact info:

- Envelope = email
- Phone = phone
- Globe = website

Font styles to use
Serif
Sans Serif

Requirements
Must have
• Professional and clean
Nice to have
• you tell me

```html
<!DOCTYPE html>
<html lang="en">
<head>
<meta charset="utf-8">
<title>TP Advisory — Business Card</title>
<link rel="stylesheet" href="https://fonts.googleapis.com/css2?family=Open+Sans:wght@400;600;700&display=swap">
<style>
  :root {
    --backdrop: #e6e6e6;
    --card-white: #ffffff;
    --brand-brown: #4f2d12;
    --ink-dark: #222222;
    --ink-muted: #5a5a5a;
    --on-brown: #ffffff;
  }
  html, body {
    margin: 0;
    padding: 0;
    width: 1200px;
    height: 987px;
    overflow: hidden;
    background: var(--backdrop);
    font-family: "Open Sans", sans-serif;
  }
  .canvas {
    position: relative;
    width: 1200px;
    height: 987px;
  }
  .card {
    position: absolute;
    width: 615px;
    height: 351px;
    box-sizing: border-box;
  }
  .card--front {
    left: 293px;
    top: 130px;
    background: var(--card-white);
  }
  .card--back {
    left: 292px;
    top: 505px;
    background: var(--brand-brown);
  }
  .edge-tab {
    position: absolute;
    left: 0;
    top: 104px;
    width: 12px;
    height: 50px;
    background: var(--brand-brown);
    border-radius: 0 25px 25px 0;
  }
  .person {
    position: absolute;
    left: 35px;
    top: 104px;
  }
  .person__name {
    margin: 0;
    font-size: 21px;
    font-weight: 600;
    color: var(--brand-brown);
    line-height: 1.2;
  }
  .person__role {
    margin: 1px 0 0;
    font-size: 15px;
    color: var(--ink-dark);
    line-height: 1.2;
  }
  .contact-list {
    position: absolute;
    left: 35px;
    top: 166px;
    margin: 0;
    padding: 0;
    list-style: none;
  }
  .contact-list__item {
    display: flex;
    align-items: center;
    gap: 8px;
    color: var(--ink-muted);
    font-size: 16px;
    line-height: 1;
    height: 24px;
  }
  .contact-list__item--phone {
    font-size: 23px;
    height: 30px;
    margin-bottom: 1px;
  }
  .contact-icon {
    width: 16px;
    height: 16px;
    flex: none;
  }
  .brand-lockup {
    position: absolute;
    left: 340px;
    top: 111px;
    width: 240px;
    display: flex;
    flex-direction: column;
    align-items: center;
    gap: 8px;
  }
  .brand-lockup__ring {
    width: 100px;
    height: 100px;
    border: 3px solid var(--brand-brown);
    border-radius: 50%;
    box-sizing: border-box;
  }
  .brand-lockup__name {
    font-size: 19px;
    font-weight: 600;
    letter-spacing: 1px;
    color: var(--brand-brown);
    text-transform: uppercase;
  }
  .back-name {
    position: absolute;
    left: 0;
    right: 0;
    top: 153px;
    text-align: center;
    font-size: 32px;
    font-weight: 600;
    letter-spacing: 2px;
    color: var(--on-brown);
    text-transform: uppercase;
  }
  .tagline {
    position: absolute;
    left: 0;
    right: 0;
    top: 270px;
    margin: 0;
    text-align: center;
    color: var(--on-brown);
    font-size: 16px;
    line-height: 23px;
  }
</style>
</head>
<body>
<main class="canvas">
  <section class="card card--front" aria-label="Card front">
    <div class="edge-tab"></div>
    <div class="person">
      <p class="person__name">Tovan Presfield</p>
      <p class="person__role">Director</p>
    </div>
    <ul class="contact-list">
      <li class="contact-list__item contact-list__item--phone">
        <svg class="contact-icon" viewBox="0 0 16 16" aria-hidden="true">
          <circle cx="8" cy="8" r="7" fill="none" stroke="#4f2d12" stroke-width="1.4"/>
          <path d="M5.3 4.4c.4-.3.9-.2 1.1.2l.6 1.2c.2.4 0 .7-.3 1l-.4.3c.4.9 1.1 1.6 2 2l.3-.4c.3-.3.6-.5 1-.3l1.2.6c.4.2.5.7.2 1.1-.6.8-1.5 1-2.4.6-1.8-.8-3.1-2.1-3.9-3.9-.4-.9-.2-1.800.6-2.4z" fill="#4f2d12"/>
        </svg>
        0427 31 94 62
      </li>
      <li class="contact-list__item">
        <svg class="contact-icon" viewBox="0 0 16 16" aria-hidden="true">
          <circle cx="8" cy="8" r="7.5" fill="#4f2d12"/>
          <rect x="4" y="5.2" width="8" height="5.6" rx="0.6" fill="#fff"/>
          <path d="M4.3 5.5 8 8.4l3.7-2.9" fill="none" stroke="#4f2d12" stroke-width="0.9"/>
        </svg>
        tovan@tp-advisory.com.au
      </li>
      <li class="contact-list__item">
        <svg class="contact-icon" viewBox="0 0 16 16" aria-hidden="true">
          <circle cx="8" cy="8" r="7.5" fill="#4f2d12"/>
          <circle cx="8" cy="8" r="4" fill="none" stroke="#fff" stroke-width="1"/>
          <ellipse cx="8" cy="8" rx="1.6" ry="4" fill="none" stroke="#fff" stroke-width="0.9"/>
          <path d="M4 8h8" stroke="#fff" stroke-width="0.9"/>
        </svg>
        www.tp-advisory.com.au
      </li>
    </ul>
    <div class="brand-lockup">
      <div class="brand-lockup__ring"></div>
      <div class="brand-lockup__name">TP Advisory</div>
    </div>
  </section>

  <section class="card card--back" aria-label="Card back">
    <div class="back-name">TP Advisory</div>
    <p class="tagline">Corporate Consulting Services<br>Clear Advice • Sound Plans • Lasting Results</p>
  </section>
</main>
</body>
</html>
```